Business Card for Jewelry Business

We need a new namecard design for a jewelry company based in Bangkok, Thailand. We have a new website recently and want the new namecard to reflect our new modern image. I have uploaded our old namecard to show you the information that needs to be on the namecard. Pls check our website www.qelburn.com for the new color scheme to help design the new namecard.

```html
<!DOCTYPE html>
<html lang="en">
<head>
<meta charset="utf-8">
<title>Qelburn Manufacturers – Business Card</title>
<link rel="stylesheet" href="https://fonts.googleapis.com/css2?family=Old+Standard+TT:wght@400;700&display=swap">
<style>
  :root {
    --teal: #52c3c8;
    --sand: #e0d8ce;
    --ink: #222222;
    --paper: #ffffff;
    --shadow: rgba(0, 0, 0, 0.13);
  }
  html, body {
    margin: 0;
    padding: 0;
    width: 1091px;
    height: 1200px;
    overflow: hidden;
    background: var(--paper);
    font-family: "Old Standard TT", "Century Schoolbook", serif;
  }
  .canvas {
    position: relative;
    width: 1091px;
    height: 1200px;
  }
  .card {
    position: absolute;
    left: 160px;
    width: 778px;
    height: 416px;
    border-radius: 56px;
    box-sizing: border-box;
    box-shadow: -6px 8px 14px var(--shadow);
  }
  .card--front {
    top: 187px;
    background: var(--teal);
  }
  .card--back {
    top: 631px;
    background: var(--paper);
    border: 5px solid var(--sand);
  }
  .emblem {
    position: absolute;
    left: 322px;
    top: 36px;
    width: 228px;
    height: 228px;
    border-radius: 50%;
    background: var(--paper);
    border: 4px solid var(--sand);
    box-sizing: border-box;
    display: flex;
    align-items: center;
    justify-content: center;
  }
  .emblem__name {
    color: var(--teal);
    font-size: 24px;
    letter-spacing: 1px;
  }
  .contact {
    position: absolute;
    display: flex;
    align-items: center;
    color: var(--paper);
    font-size: 18px;
    letter-spacing: 0.6px;
  }
  .contact__icon {
    width: 32px;
    height: 32px;
    flex: none;
    margin-right: 20px;
  }
  .contact--right .contact__icon {
    width: 30px;
    height: 30px;
    margin-right: 14px;
  }
  .contact--facebook { left: 40px; top: 306px; }
  .contact--instagram { left: 40px; top: 353px; }
  .contact--email { left: 498px; top: 305px; }
  .contact--web { left: 498px; top: 347px; }

  .brand {
    position: absolute;
    left: 40px;
    top: 180px;
    display: flex;
    align-items: center;
    color: var(--ink);
    font-size: 22px;
  }
  .brand__dot {
    width: 30px;
    height: 30px;
    border-radius: 50%;
    background: var(--teal);
    margin-right: 14px;
  }
  .person {
    position: absolute;
    left: 395px;
    color: var(--teal);
    margin: 0;
  }
  .person__name {
    top: 62px;
    font-size: 29px;
    font-weight: 700;
    line-height: 1;
  }
  .person__title {
    top: 101px;
    font-size: 18px;
    letter-spacing: 0.6px;
    line-height: 1;
  }
  .person__phones {
    top: 174px;
    font-size: 20px;
    line-height: 26px;
    letter-spacing: 0.5px;
  }
  .person__address {
    top: 273px;
    font-size: 18px;
    line-height: 25px;
    letter-spacing: 0.4px;
    font-style: normal;
  }
</style>
</head>
<body>
<main class="canvas">
  <section class="card card--front" aria-label="Card front">
    <div class="emblem"><span class="emblem__name">Qelburn</span></div>

    <div class="contact contact--facebook">
      <svg class="contact__icon" viewBox="0 0 32 32" aria-hidden="true"><circle cx="16" cy="16" r="16" fill="#fff"/></svg>
      <span>Qelburn Manufacturers</span>
    </div>
    <div class="contact contact--instagram">
      <svg class="contact__icon" viewBox="0 0 32 32" aria-hidden="true"><circle cx="16" cy="16" r="16" fill="#fff"/></svg>
      <span>QelburnMfr</span>
    </div>
    <div class="contact contact--right contact--email">
      <svg class="contact__icon" viewBox="0 0 30 30" aria-hidden="true">
        <circle cx="15" cy="15" r="15" fill="#fff"/>
        <rect x="8" y="10" width="14" height="10" fill="none" stroke="#52c3c8" stroke-width="1.6"/>
        <path d="M8 10 L15 16 L22 10 M8 20 L13 15 M22 20 L17 15" fill="none" stroke="#52c3c8" stroke-width="1.4"/>
      </svg>
      <span>hello@qelburn.com</span>
    </div>
    <div class="contact contact--right contact--web">
      <svg class="contact__icon" viewBox="0 0 30 30" aria-hidden="true">
        <circle cx="15" cy="15" r="15" fill="#fff"/>
        <text x="15" y="20" text-anchor="middle" font-size="15" fill="#52c3c8" font-family="Arial, sans-serif">@</text>
      </svg>
      <span>www.qelburn.com</span>
    </div>
  </section>

  <section class="card card--back" aria-label="Card back">
    <div class="brand"><span class="brand__dot"></span><span>Qelburn Manufacturers</span></div>

    <h1 class="person person__name">Naree Thanasok</h1>
    <p class="person person__title">Sales &amp; product development manager</p>
    <p class="person person__phones">Tel : +66 (0) 2555-0142-3<br>Fax: +662-555-0198</p>
    <address class="person person__address">128 Moo 7, Export Processing Zone 2<br>Sai Ngam Industrial Estate,<br>Bangkok, 10400 Thailand</address>
  </section>
</main>
</body>
</html>
```